Medical Cannabis company is looking for a LOGO design *

SILVER MERIDIAN (SM) is a new company in the Israeli medical cannabis industry. We will engage in PREMIUM medical cannabis growing and cultivation and also manufacturing of HIGH-END cannabis based medical products.
the design should reflect luxury, high-end and Pharma-grade products.
the design should use color GOLD and NOT using the famous cannabis leaf !

Target Market(s)

international medical cannabis Pharmaceutical companies
and of course local and international patients

Contact Information for Business Card

Ron Ben-Amit
Founder and CEO

Silver Meridian
Medical grade cannabis

ronbenamit@mailpost-example.com
972-52-3186407

Colors
ffc214
fbed22

Requirements
Must have
• clean and simple
• luxury
• gold !!
• (can also have green for Cannabis and/or blue for Pharma)
Should not have
• cannabis leaf

```html
<!DOCTYPE html>
<html lang="en">
<head>
<meta charset="utf-8">
<title>Silver Meridian — Business Card</title>
<link rel="stylesheet" href="https://fonts.googleapis.com/css2?family=Fira+Sans:wght@400;600&family=Karla:wght@400;500&display=swap">
<style>
  :root {
    --amber: #fcb82c;
    --sun-yellow: #fbed22;
    --paper: #ffffff;
    --ink-grey: #5a5a5a;
    --divider: #d6d6d6;
    --backdrop: #efeae2;
  }
  * { box-sizing: border-box; margin: 0; padding: 0; }
  html, body {
    width: 1200px; height: 1200px; overflow: hidden;
    background: var(--backdrop);
  }
  .canvas {
    width: 1200px; height: 1200px;
    display: flex; flex-direction: column;
    align-items: center; justify-content: center; gap: 60px;
  }
  .card {
    position: relative;
    width: 800px; height: 490px;
    background: var(--paper);
    overflow: hidden;
    box-shadow: 0 10px 28px rgba(0,0,0,0.14);
  }

  /* Front */
  .card-front .amber-field {
    position: absolute; left: 0; top: 0; width: 100%; height: 392px;
    background: var(--amber);
  }
  .card-front .accent-line {
    position: absolute; left: 0; top: 376px; width: 100%; height: 6px;
    background: var(--sun-yellow);
  }
  .wordmark {
    position: absolute; left: 0; top: 196px; width: 100%;
    text-align: center;
  }
  .wordmark-name {
    font-family: "Fira Sans", sans-serif;
    font-weight: 600; font-size: 42px; color: var(--paper);
    letter-spacing: 0.5px;
  }
  .wordmark-tagline {
    margin-top: 4px;
    display: flex; align-items: center; justify-content: center; gap: 12px;
    font-family: "Karla", sans-serif;
    font-weight: 500; font-size: 19px; letter-spacing: 2.4px;
    color: var(--ink-grey);
  }
  .wordmark-tagline .rule {
    width: 32px; height: 1.5px; background: var(--ink-grey);
  }

  /* Back */
  .identity {
    position: absolute; left: 0; top: 208px; width: 385px;
    text-align: center;
  }
  .person-name {
    font-family: "Fira Sans", sans-serif;
    font-weight: 600; font-size: 31px; color: var(--amber);
  }
  .person-role {
    margin-top: 2px;
    font-family: "Fira Sans", sans-serif;
    font-weight: 400; font-size: 20px; color: var(--ink-grey);
  }
  .column-divider {
    position: absolute; left: 400px; top: 168px; width: 2px; height: 152px;
    background: linear-gradient(to bottom, transparent, var(--divider) 30%, var(--divider) 70%, transparent);
  }
  .contact-list {
    position: absolute; left: 445px; top: 212px;
    list-style: none;
    font-family: "Fira Sans", sans-serif;
    font-weight: 400; font-size: 19px; color: var(--ink-grey);
  }
  .contact-list li {
    display: flex; align-items: center; gap: 14px; height: 38px;
  }
  .contact-list svg { width: 20px; height: 20px; flex: none; }
  .card-back .accent-line {
    position: absolute; left: 0; top: 406px; width: 100%; height: 6px;
    background: var(--sun-yellow);
  }
  .card-back .amber-band {
    position: absolute; left: 0; top: 418px; width: 100%; bottom: 0;
    background: var(--amber);
  }
</style>
</head>
<body>
<main class="canvas">
  <section class="card card-front" aria-label="Business card front">
    <div class="amber-field"></div>
    <div class="accent-line"></div>
    <div class="wordmark">
      <div class="wordmark-name">Silver Meridian</div>
      <div class="wordmark-tagline"><span class="rule"></span>medical grade cannabis<span class="rule"></span></div>
    </div>
  </section>

  <section class="card card-back" aria-label="Business card back">
    <div class="identity">
      <div class="person-name">Ron Ben-Amit</div>
      <div class="person-role">Founder and CEO</div>
    </div>
    <div class="column-divider"></div>
    <ul class="contact-list">
      <li>
        <svg viewBox="0 0 20 20" aria-hidden="true">
          <rect x="2" y="5" width="16" height="11" fill="var(--amber)"/>
          <path d="M2 5 L10 11 L18 5" fill="none" stroke="#ffffff" stroke-width="1.4"/>
        </svg>
        ronbenamit@mailpost-example.com
      </li>
      <li>
        <svg viewBox="0 0 20 20" aria-hidden="true">
          <path d="M5 2.5 L8 6.5 L6.5 8.5 C7.5 10.8 9.2 12.5 11.5 13.5 L13.5 12 L17.5 15 L15.5 17.5 C9 17 3 11 2.5 4.5 Z" fill="var(--amber)"/>
        </svg>
        972-52-3186407
      </li>
    </ul>
    <div class="accent-line"></div>
    <div class="amber-band"></div>
  </section>
</main>
</body>
</html>
```